Steady Valve Systems

I need a business card with the attached logo.
The second page I have attached is what we are looking for. We want doubles sided. We would like the blues fading and the logo on the back.

Industry/Entity Type

Business

```html
<!DOCTYPE html>
<html lang="en">
<head>
<meta charset="utf-8">
<title>Steady Valve Systems – Business Card</title>
<link href="https://fonts.googleapis.com/css2?family=Lato:wght@400;700;900&display=swap" rel="stylesheet">
<style>
  :root {
    --page-bg: #eceae6;
    --card-white: #ffffff;
    --brand-blue: #2b4a93;
    --brand-blue-dark: #1c3472;
    --brand-blue-light: #4a6bb8;
    --text-blue: #34539c;
    --shadow: rgba(20, 30, 60, 0.18);
  }
  * { box-sizing: border-box; margin: 0; padding: 0; }
  html, body {
    width: 1200px; height: 1023px; overflow: hidden;
    background: var(--page-bg);
    font-family: "Lato", Arial, sans-serif;
  }
  .sheet {
    width: 1200px; height: 1023px;
    display: flex; flex-direction: column;
    align-items: center; justify-content: center; gap: 60px;
  }
  .card {
    position: relative;
    width: 700px; height: 400px;
    border-radius: 4px;
    box-shadow: 0 10px 28px var(--shadow);
    overflow: hidden;
  }
  /* Front */
  .card-front { background: var(--card-white); }
  .front-shapes { position: absolute; right: 0; top: 0; width: 190px; height: 400px; }
  .front-content { position: absolute; left: 56px; top: 56px; color: var(--text-blue); }
  .brand-name {
    font-weight: 900; font-size: 40px; letter-spacing: 1px;
    color: var(--brand-blue); line-height: 1;
  }
  .person {
    margin-top: 58px; font-size: 22px; font-weight: 700;
    letter-spacing: 4px; text-transform: uppercase;
  }
  .person .role {
    font-weight: 400; letter-spacing: 0.5px; text-transform: none;
    font-size: 16px; padding-left: 12px; margin-left: 10px;
    border-left: 1.5px solid var(--text-blue);
  }
  .contacts { list-style: none; margin-top: 26px; font-size: 15px; }
  .contacts li { display: flex; align-items: center; gap: 10px; margin-bottom: 7px; }
  .contact-icon { width: 14px; height: 14px; flex: none; }
  .address { margin-top: 22px; font-size: 14px; }

  /* Back */
  .card-back {
    background: linear-gradient(120deg, var(--brand-blue-dark) 0%, var(--brand-blue) 45%, var(--brand-blue-light) 70%, var(--brand-blue-dark) 100%);
    display: flex; align-items: center; justify-content: center;
  }
  .back-brand {
    color: #ffffff; font-weight: 900; font-size: 46px; letter-spacing: 1px;
  }
</style>
</head>
<body>
<main class="sheet">
  <section class="card card-front" aria-label="Card front">
    <svg class="front-shapes" viewBox="0 0 190 400" aria-hidden="true">
      <polygon points="30,0 110,0 70,60" fill="var(--brand-blue)"/>
      <polygon points="130,0 190,0 190,90" fill="var(--brand-blue)"/>
      <polygon points="190,120 190,400 100,400 100,260" fill="var(--brand-blue)"/>
      <polygon points="80,140 180,110 80,260" fill="var(--brand-blue)"/>
    </svg>
    <div class="front-content">
      <div class="brand-name">STEADY VALVE SYSTEMS</div>
      <div class="person">Daniel Verhoef<span class="role">Director</span></div>
      <ul class="contacts">
        <li>
          <svg class="contact-icon" viewBox="0 0 14 14" aria-hidden="true"><rect width="14" height="14" rx="2" fill="var(--text-blue)"/><path d="M4 3.5l1.6-.4 1 2-1 .8a5 5 0 0 0 2.5 2.5l.8-1 2 1-.4 1.6C7 10.5 3.5 7 4 3.5z" fill="#fff"/></svg>
          +31 20 555 0187
        </li>
        <li>
          <svg class="contact-icon" viewBox="0 0 14 14" aria-hidden="true"><rect width="14" height="14" rx="2" fill="var(--text-blue)"/><rect x="3" y="4.5" width="8" height="5.5" fill="none" stroke="#fff" stroke-width="1"/><path d="M3 4.5l4 3 4-3" fill="none" stroke="#fff" stroke-width="1"/></svg>
          info@steadyvalvesystems.com
        </li>
        <li>
          <svg class="contact-icon" viewBox="0 0 14 14" aria-hidden="true"><rect width="14" height="14" rx="2" fill="var(--text-blue)"/><circle cx="7" cy="7" r="4" fill="none" stroke="#fff" stroke-width="1"/><path d="M3 7h8M7 3c-2 2.5-2 5.5 0 8M7 3c2 2.5 2 5.5 0 8" fill="none" stroke="#fff" stroke-width="0.8"/></svg>
          www.SteadyValveSystems.com
        </li>
      </ul>
      <p class="address">BV Lindengracht 48, 1015 KJ Amsterdam, The Netherlands</p>
    </div>
  </section>

  <section class="card card-back" aria-label="Card back">
    <div class="back-brand">STEADY VALVE SYSTEMS</div>
  </section>
</main>
</body>
</html>
```